Brindlecove - Healthcare Brochure - B2B

We need a new brochure design, we're satisfied with the copy but were just looking for complete overhaul of the design. Please see an example of the old design attached. It was just a template we filled out.
Requirements
Nice to have
- The second attachment is an example of a style we like

```html
<!DOCTYPE html>
<html lang="en">
<head>
<meta charset="utf-8">
<title>Brindlecove Brochure</title>
<link href="https://fonts.googleapis.com/css2?family=Poppins:wght@300;400;500;600;700;800&display=swap" rel="stylesheet">
<style>
  :root{
    --navy:#0b3a6b;
    --blue:#1a6fc6;
    --bright:#2188e6;
    --ink:#111418;
    --grey-bg:#b9b9b9;
    --card-line:#c9ced6;
    --icon-grey:#8e949c;
  }
  *{box-sizing:border-box;margin:0;padding:0}
  html,body{width:1200px;height:2700px;overflow:hidden}
  body{background:var(--grey-bg);font-family:'Poppins',sans-serif;color:var(--ink);position:relative}
  .spread{position:absolute;left:79px;width:1042px;height:768px;background:#fff;overflow:hidden;box-shadow:0 6px 18px rgba(0,0,0,.25)}
  .spread--outside{top:860px}
  .spread--inside{top:1695px}
  .abs,.photo{position:absolute}

  /* outside */
  .panel-left{left:0;top:0;width:329px;height:768px;background:linear-gradient(180deg,#eceef1 0%,#e2e8f0 45%,#b9d4f1 100%)}
  .photo-stethoscope{left:0;top:0;width:329px;height:600px;
    background:
      radial-gradient(ellipse 120px 150px at 250px 150px,#f7f8f9 0%,rgba(247,248,249,0) 100%),
      radial-gradient(ellipse 170px 260px at 80px 230px,#c9ccd0 0%,rgba(201,204,208,0) 100%),
      linear-gradient(180deg,#d9dbde 0%,#e4e6e9 45%,rgba(214,226,240,0) 100%)}
  .panel-middle{left:329px;top:0;width:330px;height:768px;background:linear-gradient(180deg,#ffffff 0%,#eef4fb 45%,#b7d4f2 100%)}
  .photo-duo{left:376px;top:415px;width:213px;height:265px;border-radius:100px 100px 0 0;
    background:
      radial-gradient(ellipse 60px 110px at 60px 180px,#f4f6f8 0%,rgba(244,246,248,0) 100%),
      radial-gradient(ellipse 65px 120px at 150px 170px,#f1f3f6 0%,rgba(241,243,246,0) 100%),
      linear-gradient(180deg,#c6d7ea 0%,#dfe6ee 40%,#eef1f4 100%)}
  .footer-band{left:0;top:680px;width:659px;height:88px;background:var(--navy)}
  .quote-card{left:30px;top:390px;width:266px;height:332px;background:#fff;border-radius:20px}
  .quote-mark{left:113px;top:363px}
  .quote-text{left:78px;top:438px;font-size:19px;line-height:21.2px;font-weight:400;color:var(--ink)}
  .quote-text .hl{color:var(--blue);font-weight:500}
  .brand{display:flex;align-items:center;justify-content:center;gap:10px;color:var(--blue);font-weight:400;font-size:27px;letter-spacing:.5px}
  .brand-dot{width:30px;height:30px;border-radius:50%;background:var(--blue)}
  .center{text-align:center}
  .col-mid{left:329px;width:330px}
  .col-right{left:659px;width:383px}
  .h-touch{font-weight:700;font-size:19px}
  .lead{font-size:14.5px;line-height:16px}
  .icon-dot{width:30px;height:30px;border-radius:50%;background:var(--blue);margin:0 auto;display:flex;align-items:center;justify-content:center}
  .contact-line{font-weight:600;font-size:14.5px;line-height:17px}
  .site{font-weight:600;font-size:15.5px;letter-spacing:1.5px}
  .tag-a{font-size:25px;font-weight:400;line-height:29px}
  .tag-b{font-size:28px;font-weight:800;line-height:31px}
  .tag-c{font-size:32px;font-weight:800;line-height:31px;color:var(--blue)}
  .rule{height:1px;background:#9aa3ad;width:80px}
  .photo-doctor{left:728px;top:130px;width:196px;height:265px;border-radius:0 60px 0 0;
    background:
      radial-gradient(ellipse 80px 110px at 100px 170px,#fbfbfc 0%,rgba(251,251,252,0) 100%),
      linear-gradient(180deg,#e6e9ec 0%,#dadfe4 100%)}

  /* inside */
  .about{left:0;top:0;width:329px;height:768px;background:linear-gradient(180deg,#bdd8f2 0%,#d6e6f6 45%,#eaf1f9 100%)}
  .photo-team{left:0;top:400px;width:329px;height:368px;
    background:
      radial-gradient(ellipse 55px 150px at 70px 230px,#f5f7f9 0%,rgba(245,247,249,0) 100%),
      radial-gradient(ellipse 55px 150px at 150px 220px,#f5f7f9 0%,rgba(245,247,249,0) 100%),
      radial-gradient(ellipse 55px 150px at 230px 225px,#f5f7f9 0%,rgba(245,247,249,0) 100%),
      radial-gradient(ellipse 40px 150px at 20px 250px,#5d9fd6 0%,rgba(93,159,214,0) 100%),
      radial-gradient(ellipse 40px 150px at 305px 250px,#5d9fd6 0%,rgba(93,159,214,0) 100%),
      linear-gradient(180deg,rgba(234,241,249,0) 0%,#dde8f3 25%,#c9d8e8 65%,#34507a 100%)}
  .section-title{font-weight:700;font-size:18.5px;letter-spacing:.2px}
  .section-title span{color:var(--blue)}
  .body-text{font-size:14px;line-height:15.2px}
  .small-text{font-size:12.5px;line-height:13.6px;color:#333}
  .vision{left:329px;top:0;width:354px;height:228px;background:var(--navy);color:#fff}
  .photo-exam{left:683px;top:0;width:283px;height:205px;border-radius:0 45px 0 0;
    background:
      radial-gradient(ellipse 60px 90px at 90px 110px,#fafbfc 0%,rgba(250,251,252,0) 100%),
      radial-gradient(ellipse 55px 80px at 175px 140px,#7b95b3 0%,rgba(123,149,179,0) 100%),
      linear-gradient(180deg,#eef0f2 0%,#dcdfe3 100%)}
  .services{left:329px;top:228px;width:713px;height:540px;background:linear-gradient(180deg,#ffffff 0%,#f4f5f7 55%,#dedfe2 100%)}
  .card{position:absolute;width:258px;height:102px;border:1.5px solid var(--card-line);border-radius:12px;background:rgba(255,255,255,.65)}
  .card-bar{position:absolute;left:20px;top:-18px;width:236px;height:32px;background:var(--blue);clip-path:polygon(0 0,89% 0,100% 100%,0 100%);color:#fff;font-weight:600;font-size:13px;line-height:32px;padding-left:22px;text-transform:uppercase;white-space:nowrap}
  .card-icon{position:absolute;left:-14px;top:-24px;width:44px;height:44px;border-radius:50%;background:var(--icon-grey);border:3px solid #fff;display:flex;align-items:center;justify-content:center}
  .card-text{position:absolute;left:30px;top:32px;font-size:14px;line-height:15.2px;color:#222;width:222px}
</style>
</head>
<body>

<section class="spread spread--outside">
  <div class="abs panel-left"></div>
  <div class="photo photo-stethoscope" role="img" aria-label="Doctor holding a stethoscope with medical icons in hexagons"></div>
  <div class="abs panel-middle"></div>
  <div class="photo photo-duo" role="img" aria-label="Two smiling doctors in white coats"></div>
  <div class="abs footer-band"></div>

  <div class="abs quote-card"></div>
  <svg class="abs quote-mark" width="80" height="56" viewBox="0 0 84 60" aria-hidden="true">
    <path d="M36 6 C18 8 6 20 6 36 C6 48 14 56 24 56 C33 56 38 50 38 42 C38 34 32 29 25 29 C22 29 19 30 17 31 C19 21 26 14 38 12 Z" fill="#fff" stroke="#1a6fc6" stroke-width="2.5"/>
    <path d="M78 6 C60 8 48 20 48 36 C48 48 56 56 66 56 C75 56 80 50 80 42 C80 34 74 29 67 29 C64 29 61 30 59 31 C61 21 68 14 80 12 Z" fill="#fff" stroke="#1a6fc6" stroke-width="2.5"/>
  </svg>
  <p class="abs quote-text">
    <span class="hl">Our process is<br>simple,<br>fast, and<br>most importantly:</span><br>
    effective.<br>One call, and we<br>take it from there.<br>From your<br>healthcare<br>facility to their home,<br>we’re there every<br>step of the way.
  </p>

  <div class="abs col-mid" style="top:56px"><div class="brand"><span class="brand-dot"></span>BRINDLECOVE</div></div>
  <h2 class="abs col-mid center h-touch" style="top:108px">GET IN TOUCH NOW</h2>
  <p class="abs col-mid center lead" style="top:134px">Join us in transforming<br>post-acute care.<br>Let’s make every patient’s<br>transition a story of success.</p>

  <div class="abs col-mid" style="top:212px">
    <div class="icon-dot"><svg width="16" height="16" viewBox="0 0 24 24"><path d="M6.6 10.8a15.1 15.1 0 0 0 6.6 6.6l2.2-2.2a1 1 0 0 1 1-.25 11.4 11.4 0 0 0 3.6.57 1 1 0 0 1 1 1V20a1 1 0 0 1-1 1A17 17 0 0 1 3 4a1 1 0 0 1 1-1h3.5a1 1 0 0 1 1 1c0 1.25.2 2.45.57 3.57a1 1 0 0 1-.25 1z" fill="#fff"/></svg></div>
  </div>
  <p class="abs col-mid center contact-line" style="top:245px">555-014-2731</p>
  <div class="abs col-mid" style="top:275px">
    <div class="icon-dot"><svg width="16" height="16" viewBox="0 0 24 24"><rect x="6" y="3" width="12" height="6" fill="#fff"/><rect x="3" y="10" width="18" height="11" rx="2" fill="#fff"/><rect x="7" y="14" width="10" height="2" fill="#1a6fc6"/><rect x="7" y="17" width="10" height="2" fill="#1a6fc6"/></svg></div>
  </div>
  <p class="abs col-mid center contact-line" style="top:307px">555-014-8860</p>
  <div class="abs col-mid" style="top:337px">
    <div class="icon-dot"><svg width="14" height="16" viewBox="0 0 24 28"><path d="M12 1a9 9 0 0 0-9 9c0 7 9 17 9 17s9-10 9-17a9 9 0 0 0-9-9z" fill="#fff"/><circle cx="12" cy="10" r="3.5" fill="#1a6fc6"/></svg></div>
  </div>
  <p class="abs col-mid center contact-line" style="top:369px">18 Harbor Ln, Ste 210,<br>Millbrook, MA, 01990</p>
  <p class="abs col-mid center site" style="top:702px;color:#fff">www.brindlecove.com</p>

  <div class="abs col-right" style="top:52px"><div class="brand" style="font-size:30px"><span class="brand-dot"></span>BRINDLECOVE</div></div>
  <div class="abs" style="left:691px;top:123px;width:271px;height:307px;background:var(--blue);border-radius:0 95px 0 0"></div>
  <div class="abs" style="left:691px;top:380px;width:135px;height:50px;background:var(--navy)"></div>
  <div class="photo photo-doctor" role="img" aria-label="Female doctor in a white coat with arms crossed"></div>

  <div class="abs col-right center" style="top:458px">
    <p class="tag-a">BridgingGaps.<br>ImprovingLives.</p>
    <p class="tag-b" style="margin-top:3px">REVOLUTIONIZING</p>
    <p class="tag-c">POST-ACUTE</p>
    <div style="display:flex;align-items:center;justify-content:center;gap:8px">
      <span class="rule"></span><span class="tag-c">CARE</span><span class="rule"></span>
    </div>
    <p style="font-weight:700;font-size:18px;margin-top:12px">ONE PATIENT AT A TIME</p>
    <p style="font-size:14px;line-height:16px">Because every patient deserves a<br>seamless recovery.</p>
  </div>
  <p class="abs col-right center site" style="top:702px">www.<span style="color:var(--blue)">brindlecove</span>.com</p>
</section>

<section class="spread spread--inside">
  <div class="abs about"></div>
  <div class="photo photo-team" role="img" aria-label="Group of smiling doctors and nurses in white coats and scrubs"></div>
  <h2 class="abs section-title" style="left:37px;top:40px">ABOUT <span>BRINDLECOVE</span></h2>
  <p class="abs body-text" style="left:37px;top:78px;width:245px">At Brindlecove, we don’t just bridge the gap. We transform the journey into a smooth, seamless experience, from the moment a patient discharges from your facility until their appointment with a primary care physician. For Medicare beneficiaries, that’s life-changing.</p>
  <div class="abs" style="left:41px;top:226px;width:1px;height:66px;background:#555"></div>
  <p class="abs small-text" style="left:57px;top:226px;width:225px">Delivering personalized, seamless care that empowers patients, reduces readmissions, and ensures smooth recovery from healthcare facility to home</p>

  <div class="abs vision"></div>
  <h2 class="abs section-title" style="left:364px;top:40px;color:#fff">OUR <span style="color:var(--bright)">VISION</span></h2>
  <p class="abs body-text" style="left:364px;top:78px;width:260px;color:#fff">To make the healthcare experience for every patient as fluid, efficient, and compassionate as possible.</p>
  <p class="abs body-text" style="left:364px;top:136px;width:265px;color:#fff">Through cutting-edge care and seamless coordination, we ensure patients recover faster, stay healthier, and never lose sight of their well-being.</p>
  <div class="abs" style="left:683px;top:0;width:359px;height:228px;background:var(--bright)"></div>
  <div class="photo photo-exam" role="img" aria-label="Doctor listening to an older woman's heart with a stethoscope"></div>
  <div class="abs" style="left:683px;top:180px;width:160px;height:48px;background:var(--blue);border-radius:0 30px 0 0"></div>

  <div class="abs services"></div>

  <div class="card" style="left:374px;top:290px">
    <div class="card-bar">Seamless Transition</div>
    <div class="card-icon"><svg width="20" height="20" viewBox="0 0 24 24"><circle cx="12" cy="12" r="8" fill="none" stroke="#fff" stroke-width="2"/><path d="M8 12h8M13 9l3 3-3 3" stroke="#fff" stroke-width="2" fill="none"/></svg></div>
    <p class="card-text">We ensure smooth facility-to home transitions with no gaps in care, prioritizing patient outcomes.</p>
  </div>
  <div class="card" style="left:688px;top:290px">
    <div class="card-bar">VNA Order Sign-Off</div>
    <div class="card-icon"><svg width="20" height="20" viewBox="0 0 24 24"><rect x="3" y="5" width="10" height="14" rx="1" fill="none" stroke="#fff" stroke-width="2"/><path d="M10 12h10M17 9l3 3-3 3" stroke="#fff" stroke-width="2" fill="none"/></svg></div>
    <p class="card-text">We sign off on VNA orders, streamlining the process and ensuring seamless home care coordination.</p>
  </div>
  <div class="card" style="left:374px;top:437px">
    <div class="card-bar">Prescription Refills</div>
    <div class="card-icon"><svg width="20" height="20" viewBox="0 0 24 24"><path d="M6 3h9l4 4v14H6z" fill="none" stroke="#fff" stroke-width="2"/><path d="M9 12h6M12 9v6" stroke="#fff" stroke-width="2"/></svg></div>
    <p class="card-text">We handle refills for non-controlled prescriptions, ensuring your patients have what they need to recover.</p>
  </div>
  <div class="card" style="left:688px;top:437px">
    <div class="card-bar" style="font-size:12px;letter-spacing:-.2px">Streamlined Referral Process</div>
    <div class="card-icon"><svg width="20" height="20" viewBox="0 0 24 24"><circle cx="9" cy="9" r="3" fill="#fff"/><circle cx="16" cy="14" r="3" fill="#fff"/><circle cx="12" cy="12" r="9" fill="none" stroke="#fff" stroke-width="1.6"/></svg></div>
    <p class="card-text">Easily refer patients with a fast, simple process that ensures seamless transitions in care.</p>
  </div>
  <div class="card" style="left:374px;top:585px">
    <div class="card-bar">Reduced Readmission Risk</div>
    <div class="card-icon"><svg width="20" height="20" viewBox="0 0 24 24"><path d="M3 12l9-8 9 8M6 10v10h12V10" fill="none" stroke="#fff" stroke-width="2"/><path d="M10 15h4M12 13v4" stroke="#fff" stroke-width="2"/></svg></div>
    <p class="card-text">We minimize readmission risk with proactive care, enhancing outcomes and supporting value based care goals.</p>
  </div>
  <div class="card" style="left:688px;top:585px">
    <div class="card-bar">Patient Education</div>
    <div class="card-icon"><svg width="20" height="20" viewBox="0 0 24 24"><circle cx="8" cy="6" r="2.5" fill="#fff"/><circle cx="16" cy="6" r="2.5" fill="#fff"/><path d="M5 11h6v10H5zM13 11h6v10h-6z" fill="#fff"/></svg></div>
    <p class="card-text">Empowering patient’s with information to make informed decisions about their health.</p>
  </div>
</section>

</body>
</html>
```